Looking for something sharp classy and with an edge for an advanced civil construction business
Something that says professional
nothing too DARK

Target Market(s)

mining companies council civil contractors concrete works

Industry/Entity Type

Construction

Contact Information for Business Card

Ridgeline Civil Constructions
ridgelinecivilconstruction@mailtrove.net
Rewi Ashdown
0412758391

Font styles to use
Serif
Sans Serif

Colors
0455a3
0592cd
85cae6
000000
919191

Requirements
Must have
• On the back of the card must have
down the bottom small print email logo phone number

Should not have
• follow us on facebook
Ridgeline Civil Constructions

follow us on instagram
RIDGELINECIVILCONSTRUCTIONS

```html
<!DOCTYPE html>
<html lang="en">
<head>
<meta charset="utf-8">
<title>Ridgeline Civil Constructions – Business Card</title>
<link rel="stylesheet" href="https://fonts.googleapis.com/css2?family=Arimo:wght@400;700&display=swap">
<style>
  :root {
    --backdrop: #eef3f7;
    --blue-deep: #0455a3;
    --blue-bright: #0592cd;
    --blue-pale: #85cae6;
    --ink-black: #000000;
    --ink-grey: #919191;
    --ink-white: #ffffff;
    --ink-soft: #e8f4fa;
    --band-white: #f7f9fa;
  }
  * { box-sizing: border-box; margin: 0; padding: 0; }
  html, body {
    width: 1200px;
    height: 1200px;
    overflow: hidden;
  }
  body {
    background: var(--backdrop);
    font-family: "Arimo", Arial, sans-serif;
    display: flex;
    flex-direction: column;
    align-items: center;
    justify-content: center;
    gap: 60px;
  }
  .card {
    position: relative;
    width: 900px;
    height: 514px;
    overflow: hidden;
    box-shadow: 0 10px 30px rgba(4, 85, 163, 0.25);
  }

  /* Front */
  .card--front {
    background: linear-gradient(135deg, var(--blue-deep) 0%, var(--blue-bright) 100%);
  }
  .brand {
    position: absolute;
    color: var(--ink-white);
    font-weight: 700;
    text-transform: uppercase;
    line-height: 1;
    white-space: nowrap;
  }
  .card--front .brand { left: 68px; top: 60px; }
  .brand__name { display: block; font-size: 96px; letter-spacing: 1px; }
  .brand__tagline { display: block; font-size: 38px; margin-top: 10px; letter-spacing: 0.5px; color: var(--ink-soft); }
  .rule {
    position: absolute;
    left: 0;
    right: 0;
    top: 232px;
    height: 4px;
    border-top: 1px solid var(--blue-pale);
    border-bottom: 1px solid var(--blue-deep);
  }
  .holder {
    position: absolute;
    left: 90px;
    top: 278px;
    color: var(--ink-white);
  }
  .holder__name { font-size: 34px; font-weight: 400; margin-bottom: 30px; }
  .contact { list-style: none; }
  .contact__item {
    display: flex;
    align-items: center;
    gap: 16px;
    font-size: 24px;
    margin-bottom: 22px;
    padding-left: 50px;
    white-space: nowrap;
  }
  .icon { width: 26px; height: 26px; flex: none; fill: currentColor; }

  /* Back */
  .card--back { background: var(--band-white); }
  .back__top {
    position: absolute;
    left: 0; top: 0; right: 0;
    height: 350px;
    background: linear-gradient(135deg, var(--blue-deep) 0%, var(--blue-bright) 100%);
    border-bottom: 4px solid var(--blue-pale);
  }
  .card--back .brand { left: 96px; top: 56px; }
  .card--back .brand__name { font-size: 120px; }
  .card--back .brand__tagline { font-size: 44px; margin-top: 14px; }
  .back__band {
    position: absolute;
    left: 0; right: 0; bottom: 0;
    height: 164px;
    display: flex;
    align-items: center;
    justify-content: space-between;
    padding: 0 50px 0 46px;
    color: var(--ink-black);
  }
  .band-mark {
    font-size: 40px;
    font-weight: 700;
    color: var(--ink-grey);
    letter-spacing: 1px;
  }
  .back__band .contact__item {
    font-size: 22px;
    padding-left: 0;
    margin-bottom: 14px;
    gap: 12px;
  }
  .back__band .contact__item:last-child { margin-bottom: 0; }
  .back__band .icon { width: 22px; height: 22px; color: var(--blue-deep); }
</style>
</head>
<body>

<svg width="0" height="0" style="position:absolute" aria-hidden="true">
  <symbol id="icon-phone" viewBox="0 0 24 24">
    <path d="M6.6 10.8a15.2 15.2 0 0 0 6.6 6.6l2.2-2.2a1 1 0 0 1 1-.25 11.4 11.4 0 0 0 3.6.57 1 1 0 0 1 1 1V20a1 1 0 0 1-1 1A17 17 0 0 1 3 4a1 1 0 0 1 1-1h3.5a1 1 0 0 1 1 1c0 1.25.2 2.45.57 3.57a1 1 0 0 1-.25 1z"/>
  </symbol>
  <symbol id="icon-mail" viewBox="0 0 24 24">
    <path d="M2 6.2V19h20V6.2l-10 7.6z"/>
    <path d="M2.6 5h18.8L12 12.2z"/>
  </symbol>
</svg>

<section class="card card--front" aria-label="Business card front">
  <div class="brand">
    <span class="brand__name">Ridgeline</span>
    <span class="brand__tagline">Civil Constructions Ltd</span>
  </div>
  <div class="rule"></div>
  <div class="holder">
    <p class="holder__name">Rewi Ashdown</p>
    <ul class="contact">
      <li class="contact__item"><svg class="icon"><use href="#icon-phone"/></svg>0412758391</li>
      <li class="contact__item"><svg class="icon"><use href="#icon-mail"/></svg>ridgelinecivilconstruction@mailtrove.net</li>
    </ul>
  </div>
</section>

<section class="card card--back" aria-label="Business card back">
  <div class="back__top">
    <div class="brand">
      <span class="brand__name">Ridgeline</span>
      <span class="brand__tagline">Civil Constructions Ltd</span>
    </div>
  </div>
  <div class="back__band">
    <span class="band-mark">RIDGELINE</span>
    <ul class="contact">
      <li class="contact__item"><svg class="icon"><use href="#icon-phone"/></svg>0412758391</li>
      <li class="contact__item"><svg class="icon"><use href="#icon-mail"/></svg>ridgelinecivilconstruction@mailtrove.net</li>
    </ul>
  </div>
</section>

</body>
</html>
```